New Business Card Design Project

We are looking for a talented individual to create a truly awesome/unique business card design for us. We are looking for a someone to design something that will really stand out from the crowd - we don't mind what ideas you come up with (ie embossed/flat/matte/shine etc etc) just wow us with your creativity.
Updates

Target Market(s)

Video Games Industry Professionals (all levels of seniority from QA Testers through to CEOs)

Contact Information for Business Card

Company logo (see upload)
Company name: Northbay Play Careers Ltd
Employee Name: Darren Elsby
Job title: CEO
Website: www.nbpc2go.example
Office +44 1632 960418
Mobile: +44 7700 900276
Email: darren@nbpc2go.example

Colors

Designer to choose colors to be used in the design.

Requirements
Must have
• The business card design MUST contain all the information listed in the BUSINESS CARD DETAILS box.
• You will see the colours that are relevant to us (ie company logo) in the uploaded imagery - however you do not have to use all these colours when designing the business card itself
• MUST BE DOUBLE SIDED

```html
<!DOCTYPE html>
<html lang="en">
<head>
<meta charset="utf-8">
<title>Northbay Play Careers – Business Card</title>
<link rel="stylesheet" href="https://fonts.googleapis.com/css2?family=Open+Sans:wght@400;700;800&display=swap">
<style>
  :root {
    --backdrop: #ececec;
    --card-core: #2b2a85;
    --card-edge: #15144f;
    --pink: #ec1c8c;
    --cyan: #31b8e6;
    --white: #ffffff;
  }
  * { margin: 0; padding: 0; box-sizing: border-box; }
  html, body { width: 1200px; height: 1200px; overflow: hidden; }
  body {
    position: relative;
    background: var(--backdrop);
    font-family: "Open Sans", Arial, sans-serif;
  }
  .card {
    position: absolute;
    left: 180px;
    width: 840px;
    height: 480px;
    border-radius: 22px;
    background: radial-gradient(ellipse at 50% 45%, var(--card-core) 0%, var(--card-edge) 100%);
    overflow: hidden;
  }
  .card--front { top: 70px; }
  .card--back { top: 654px; }

  .brand {
    position: absolute;
    left: 130px;
    top: 170px;
    display: flex;
    align-items: center;
    gap: 34px;
  }
  .brand__dot {
    width: 130px;
    height: 130px;
    border-radius: 50%;
    background: var(--white);
    flex: none;
  }
  .brand__name {
    color: var(--white);
    font-weight: 800;
    font-size: 44px;
    line-height: 1.05;
  }

  .identity {
    position: absolute;
    left: 50px;
    top: 170px;
    width: 420px;
    text-align: center;
  }
  .identity__name {
    color: var(--white);
    font-weight: 800;
    font-size: 48px;
    letter-spacing: 1px;
    white-space: nowrap;
    text-shadow: -4px -2px 0 var(--pink), 4px 3px 0 var(--cyan);
  }
  .identity__role {
    margin-top: 6px;
    color: var(--cyan);
    font-size: 24px;
  }

  .divider {
    position: absolute;
    left: 518px;
    top: 140px;
    width: 2px;
    height: 196px;
    background: var(--pink);
  }

  .contacts {
    position: absolute;
    left: 552px;
    top: 160px;
    width: 260px;
    list-style: none;
  }
  .contacts__item {
    display: flex;
    align-items: center;
    gap: 12px;
    height: 43px;
    color: var(--cyan);
    font-size: 17px;
    white-space: nowrap;
  }
  .contacts__icon { width: 18px; height: 20px; flex: none; }
</style>
</head>
<body>

<section class="card card--front" aria-label="Card front">
  <div class="brand">
    <span class="brand__dot"></span>
    <span class="brand__name">Northbay Play<br>Careers</span>
  </div>
</section>

<section class="card card--back" aria-label="Card back">
  <div class="identity">
    <div class="identity__name">DARREN ELSBY</div>
    <div class="identity__role">CEO</div>
  </div>

  <div class="divider"></div>

  <ul class="contacts">
    <li class="contacts__item">
      <svg class="contacts__icon" viewBox="0 0 18 20" aria-hidden="true">
        <rect x="1" y="4" width="16" height="12" fill="#ec1c8c"/>
        <path d="M1 4 L9 11 L17 4" fill="none" stroke="#2b2a85" stroke-width="1.5"/>
      </svg>
      darren@nbpc2go.example
    </li>
    <li class="contacts__item">
      <svg class="contacts__icon" viewBox="0 0 18 20" aria-hidden="true">
        <rect x="4" y="1" width="10" height="18" rx="1.5" fill="none" stroke="#ec1c8c" stroke-width="1.5"/>
        <line x1="7" y1="16" x2="11" y2="16" stroke="#ec1c8c" stroke-width="1.5"/>
      </svg>
      +44 1632 960418
    </li>
    <li class="contacts__item">
      <svg class="contacts__icon" viewBox="0 0 18 20" aria-hidden="true">
        <path d="M4 3 L7 3 L8 7 L6 8.5 C7 11 9 13 11.5 14 L13 12 L17 13 L17 16 C17 17 16 18 15 18 C8 17 3 12 2 5 C2 4 3 3 4 3 Z" fill="#ec1c8c"/>
      </svg>
      +44 7700 900276
    </li>
    <li class="contacts__item">
      <svg class="contacts__icon" viewBox="0 0 18 20" aria-hidden="true">
        <circle cx="9" cy="10" r="7.5" fill="none" stroke="#ec1c8c" stroke-width="1.5"/>
        <ellipse cx="9" cy="10" rx="3.2" ry="7.5" fill="none" stroke="#ec1c8c" stroke-width="1.2"/>
        <line x1="1.5" y1="10" x2="16.5" y2="10" stroke="#ec1c8c" stroke-width="1.2"/>
      </svg>
      www.nbpc2go.example
    </li>
  </ul>
</section>

</body>
</html>
```